A webite for an Urgent Care for children

We need a design for a new website for an Urgent care for kids. We are based in Atlanta, GA and provide quality after-hours and urgent care services for children. We will appreciate an innovative design that employs flash technology, especially on the Home page. We also want there to be a Contact Us form. There should also be a control panel with the ability for us to make quick and minor edits on the website as needed without requiring the services of an expert.

Target Market(s)

Parents, children, general audience

Industry/Entity Type

Healthcare

Coding

Coded - Design and coding required

Number of Pages Required

5+ page

Font styles to use
Sans Serif
Decorative

Colors
acd037
acd136
cadf82
eaf2ce
f6faec

Requirements
Must have
• Mobile devices website capable
• Link to social media, Facebook, twitter, etc
Nice to have
• Ability for customers to pay online.

```html
<!DOCTYPE html>
<html lang="en">
<head>
<meta charset="utf-8">
<title>SUNNYSIDE Urgent Care</title>
<link href="https://fonts.googleapis.com/css2?family=Fredoka:wght@600&family=Oswald:wght@400&family=Patrick+Hand&family=Open+Sans:wght@400;600&display=swap" rel="stylesheet">
<style>
:root{
  --green:#acd037;
  --green-2:#acd136;
  --green-soft:#cadf82;
  --green-pale:#eaf2ce;
  --green-mist:#f6faec;
  --sky:#2d8fc4;
  --sky-deep:#1a5f93;
  --sun:#f7e43a;
  --ink:#1d1d1d;
  --text:#333;
  --muted:#777;
  --star:#f2b705;
  --white:#fff;
  --night:#0d0d0d;
}
*{box-sizing:border-box;margin:0;padding:0}
html,body{width:1200px;height:3010px;overflow:hidden}
body{position:relative;background:var(--white);font-family:"Open Sans",Arial,sans-serif;color:var(--text)}
.abs{position:absolute}

/* header */
.site-header{left:0;top:0;width:1200px;height:300px;background:radial-gradient(ellipse at 50% 10%,#5ab4e0 0%,var(--sky) 45%,var(--sky-deep) 100%)}
.header-art{left:0;top:150px;width:1200px;height:150px;background:linear-gradient(180deg,rgba(255,255,255,0) 0%,rgba(255,255,255,.15) 40%,#8bc34a 78%,#6fa83a 100%)}
.cart-count{left:70px;top:6px;font-size:12px;color:var(--white);display:flex;align-items:center;gap:6px}
.social{right:82px;top:6px;display:flex;gap:9px}
.social span{width:13px;height:13px;border-radius:50%;background:var(--white);display:block}
.brand{left:0;top:100px;width:1200px;text-align:center;font-family:"Fredoka",Arial,sans-serif;font-weight:600;font-size:48px;color:var(--sun)}

.main-nav{left:66px;top:300px;width:1052px;height:50px;background:var(--green);display:flex;align-items:center;padding-left:92px;gap:0}
.main-nav a{font-family:"Oswald",Arial,sans-serif;font-size:19px;color:var(--white);text-decoration:none;margin-right:60px}

/* hero */
.hero{left:0;top:350px;width:1200px;height:527px;background:linear-gradient(100deg,#e9d9c4 0%,#f3e6d2 30%,#d9cbb6 55%,#b9c6a3 80%,#8fae6a 100%)}
.hero-arrow{top:242px;width:66px;height:50px;background:#d7b98a;border:3px solid #a9844f;border-radius:6px;display:flex;align-items:center;justify-content:center}
.hero-arrow.prev{left:70px}
.hero-arrow.next{right:62px}
.hero-caption{left:297px;top:326px;width:604px;height:149px;background:var(--green);color:var(--white);font-family:"Patrick Hand",cursive;font-size:46px;line-height:50px;text-align:center;padding-top:24px}

/* welcome */
.section-title{left:0;width:1200px;text-align:center;font-family:"Patrick Hand",cursive;font-size:56px;color:var(--ink);letter-spacing:1px}
.section-title em{font-style:normal;color:var(--green)}
.welcome-title{top:925px}
.welcome-copy{left:130px;top:1012px;width:940px;text-align:center;font-size:13.5px;line-height:27px;color:var(--ink)}
.welcome-copy p+p{margin-top:18px}
.btn-green{left:502px;top:1281px;width:196px;height:38px;background:var(--green);color:var(--ink);font-size:14px;font-weight:600;display:flex;align-items:center;justify-content:center}

.featured-title{top:1378px}
.featured-sub{left:0;top:1458px;width:1200px;text-align:center;font-size:11.5px;color:var(--muted)}
.featured-rule{left:570px;top:1485px;width:60px;height:2px;background:var(--green)}

/* products */
.product{width:253px;height:362px;border:2px solid var(--green-soft);background:var(--green-mist)}
.product-photo{position:absolute;left:0;top:0;width:249px;height:251px;background:var(--white);display:flex;align-items:center;justify-content:center}
.product-photo i{display:block;width:150px;height:110px;border-radius:40px;opacity:.85}
.badge{position:absolute;left:0;top:0;background:var(--green);color:var(--white);font-size:10px;font-weight:600;padding:2px 6px;z-index:2}
.quick{position:absolute;right:12px;top:142px;display:flex;flex-direction:column;gap:4px}
.quick span{width:26px;height:26px;background:var(--green);display:flex;align-items:center;justify-content:center}
.product-name{position:absolute;left:18px;top:276px;font-size:15px;color:var(--ink)}
.price{position:absolute;left:18px;top:320px;width:64px;height:22px;background:var(--green);color:var(--ink);font-size:11px;font-weight:600;display:flex;align-items:center;justify-content:center}
.stars{position:absolute;right:18px;top:320px;font-size:12px;letter-spacing:3px;color:var(--star)}

/* footer */
.footer-wave{left:0;top:2360px;width:1200px;height:120px}
.site-footer{left:0;top:2470px;width:1200px;height:490px;background:var(--green)}
.foot-title{font-family:"Patrick Hand",cursive;font-size:24px;color:var(--white);letter-spacing:1px}
.payments{left:164px;top:88px;display:flex;gap:10px}
.payments span{width:36px;height:20px;border-radius:3px;background:rgba(255,255,255,.55)}
.phones{left:686px;top:84px;display:flex;gap:50px;color:var(--white);font-size:17px}
.phones span{display:flex;align-items:center;gap:8px}
.foot-rule{left:66px;top:150px;width:1052px;height:1px;background:rgba(255,255,255,.45)}
.col{top:192px}
.col ul{list-style:none;margin-top:18px}
.col li{font-size:13px;color:var(--ink);height:33px;display:flex;align-items:center;gap:10px}
.about-copy{font-size:12px;line-height:22px;color:var(--ink);width:330px;margin-top:18px}
.btn-dark{left:66px;top:420px;width:82px;height:28px;background:var(--night);color:var(--white);font-size:12px;font-weight:600;display:flex;align-items:center;justify-content:center}
.foot-icons{display:flex;gap:16px;margin-top:8px}
.foot-icons span{width:12px;height:12px;border-radius:50%;background:var(--ink);display:block}
.copyright{left:0;top:2960px;width:1200px;height:50px;background:var(--night);color:var(--white);font-size:13px;display:flex;align-items:center;justify-content:center}
</style>
</head>
<body>

<header class="abs site-header" role="img" aria-label="Header illustration: blue sky with sun rays, clouds, a toy train, rocking horse, toy car and teddy bear on grass">
  <div class="abs header-art"></div>
  <div class="abs cart-count">
    <svg width="14" height="12" viewBox="0 0 14 12"><path d="M0 1h3l2 7h7l2-5H4" fill="none" stroke="#fff" stroke-width="1.4"/><circle cx="6" cy="10.5" r="1.2" fill="#fff"/><circle cx="11" cy="10.5" r="1.2" fill="#fff"/></svg>
    Cart Items : 1
  </div>
  <div class="abs social"><span></span><span></span><span></span><span></span><span></span><span></span></div>
  <div class="abs brand">SUNNYSIDE Urgent Care</div>
</header>

<nav class="abs main-nav">
  <a href="#">Home</a><a href="#">About Us</a><a href="#">Our Services</a><a href="#">Finance and Insurance</a><a href="#">Office Forms</a><a href="#">Contact Us</a><a href="#">FAQ</a>
</nav>

<section class="abs hero" role="img" aria-label="Photo of a smiling young girl resting her chin on her hands among colourful wooden toys">
  <div class="abs hero-arrow prev"><svg width="30" height="20" viewBox="0 0 30 20"><path d="M28 10H4M12 2 4 10l8 8" fill="none" stroke="#6b4a22" stroke-width="3"/></svg></div>
  <div class="abs hero-arrow next"><svg width="30" height="20" viewBox="0 0 30 20"><path d="M2 10h24M18 2l8 8-8 8" fill="none" stroke="#6b4a22" stroke-width="3"/></svg></div>
  <div class="abs hero-caption">Play, Learn &amp; Grow<br>Kindly Playground Center</div>
</section>

<h1 class="abs section-title welcome-title">Welcome to <em>Sunnyside</em></h1>
<div class="abs welcome-copy">
  <p>He attended the renowned Harborview College of Medicine, Nigeria, where he obtained his medical degree. As Delta Chief, head of the most prestigious club in all of West Africa, his philanthropic activities included helping fellow students in need. In the early days of his career, he collaborated with the Global Health Alliance and the Nigerian government in combating an outbreak of yellow fever in some rural communities during his National Service. He is married to Lena, an accountant, and together they have three lovely children.</p>
  <p>Dr. Amari and his family spent five years in Westbrook, during which time he also completed his residency in Pediatrics at Westbrook State University. His desire was to work with Christian believers and was led to the Atlanta area where he teamed up with a group of pediatricians in Fayetteville for two years.</p>
</div>
<div class="abs btn-green">Read More</div>

<h2 class="abs section-title featured-title">Featured <em>Items</em></h2>
<div class="abs featured-sub">Listed below our best seller items with carousel widget</div>
<div class="abs featured-rule"></div>

<!-- row 1 -->
<article class="abs product" style="left:66px;top:1547px">
  <span class="badge">BEST SELLING</span>
  <div class="product-photo" role="img" aria-label="Toy learning laptop"><i style="background:linear-gradient(#e23b3b,#2a49b8)"></i></div>
  <div class="quick">
    <span><svg width="14" height="12" viewBox="0 0 14 12"><path d="M0 1h3l2 7h7l2-5H4" fill="none" stroke="#fff" stroke-width="1.4"/></svg></span>
    <span><svg width="12" height="11" viewBox="0 0 12 11"><path d="M6 10 1 5a2.6 2.6 0 0 1 5-3 2.6 2.6 0 0 1 5 3z" fill="none" stroke="#fff" stroke-width="1.3"/></svg></span>
    <span><svg width="14" height="10" viewBox="0 0 14 10"><path d="M1 5q6-7 12 0-6 7-12 0z" fill="none" stroke="#fff" stroke-width="1.3"/><circle cx="7" cy="5" r="1.6" fill="#fff"/></svg></span>
  </div>
  <div class="product-name">Nullami tincidunte</div><div class="price">$80.00</div><div class="stars">★★★★★</div>
</article>
<article class="abs product" style="left:332px;top:1547px">
  <div class="product-photo" role="img" aria-label="Colourful toy train of building blocks"><i style="background:linear-gradient(90deg,#e8443a,#f4c430,#3bb04a,#2f7fd8);height:60px"></i></div>
  <div class="product-name">Malesuada mi</div><div class="price">$40.00</div><div class="stars">★★★★★</div>
</article>
<article class="abs product" style="left:598px;top:1547px">
  <div class="product-photo" role="img" aria-label="Baby activity walker toy"><i style="background:linear-gradient(#8bc34a,#e0e0e0,#6a3fa0)"></i></div>
  <div class="product-name">Phasellus a arcua</div><div class="price">$20.00</div><div class="stars">★★★★★</div>
</article>
<article class="abs product" style="left:864px;top:1547px">
  <span class="badge">BEST SELLING</span>
  <div class="product-photo" role="img" aria-label="Pink toy car"><i style="background:linear-gradient(#f47c8a,#e2536a)"></i></div>
  <div class="product-name">Curabitur sodales</div><div class="price">$140.00</div><div class="stars">★★★★★</div>
</article>

<!-- row 2 -->
<article class="abs product" style="left:66px;top:1927px">
  <span class="badge">BEST SELLING</span>
  <div class="product-photo" role="img" aria-label="Baby activity walker toy"><i style="background:linear-gradient(#8bc34a,#e0e0e0,#6a3fa0)"></i></div>
  <div class="product-name">Nullami tincidunte</div><div class="price">$80.00</div><div class="stars">★★★★★</div>
</article>
<article class="abs product" style="left:332px;top:1927px">
  <div class="product-photo" role="img" aria-label="Pink toy car"><i style="background:linear-gradient(#f47c8a,#e2536a)"></i></div>
  <div class="product-name">Malesuada mi</div><div class="price">$40.00</div><div class="stars">★★★★★</div>
</article>
<article class="abs product" style="left:598px;top:1927px">
  <span class="badge">BEST SELLING</span>
  <div class="product-photo" role="img" aria-label="Toy learning laptop"><i style="background:linear-gradient(#e23b3b,#2a49b8)"></i></div>
  <div class="product-name">Phasellus a arcua</div><div class="price">$20.00</div><div class="stars">★★★★★</div>
</article>
<article class="abs product" style="left:864px;top:1927px">
  <div class="product-photo" role="img" aria-label="Colourful toy train of building blocks"><i style="background:linear-gradient(90deg,#e8443a,#f4c430,#3bb04a,#2f7fd8);height:60px"></i></div>
  <div class="product-name">Curabitur sodales</div><div class="price">$140.00</div><div class="stars">★★★★★</div>
</article>

<svg class="abs footer-wave" viewBox="0 0 1200 120" role="img" aria-label="Playful footer border with scattered toys: blocks, ball, puzzle pieces, rocking horse and alarm clock">
  <path d="M0 70 Q150 30 300 60 T600 55 T900 60 T1200 50 V120 H0Z" fill="var(--green)"/>
</svg>

<footer class="abs site-footer">
  <div class="abs foot-title" style="left:220px;top:36px">Payment Methods</div>
  <div class="abs payments"><span></span><span></span><span></span><span></span><span></span><span></span><span></span></div>

  <div class="abs foot-title" style="left:736px;top:36px">We're Available 24/7</div>
  <div class="abs phones">
    <span><svg width="16" height="16" viewBox="0 0 16 16"><path d="M3 1l3 3-2 2q2 4 6 6l2-2 3 3-2 2Q6 15 1 3z" fill="#fff"/></svg>+00 555 01 23</span>
    <span><svg width="18" height="16" viewBox="0 0 18 16"><path d="M1 6q8-6 16 0l-2 2-3-1V5H6v2L3 8z" fill="#fff"/><rect x="4" y="9" width="10" height="6" rx="1" fill="#fff"/></svg>+00 555 01 45</span>
  </div>
  <div class="abs foot-rule"></div>

  <div class="abs col" style="left:66px">
    <div class="foot-title">We Are Urgent Care</div>
    <p class="about-copy">Welcome to SUNNYSIDE Urgent Care, your after-hours pediatric urgent care. We are here when your little ones suddenly wake up sick or sustain an injury and you need immediate medical attention, but your regular doctor's office is closed. We are unique in the services we provide and are an alternative when your child needs.</p>
  </div>
  <div class="abs col" style="left:464px">
    <div class="foot-title">Main Links</div>
    <ul><li>Home</li><li>About Us</li><li>Our Services</li><li>Office Forms</li><li>Contact Us</li></ul>
  </div>
  <div class="abs col" style="left:692px">
    <div class="foot-title">Get In Touch</div>
    <ul>
      <li><svg width="14" height="10" viewBox="0 0 14 10"><rect width="14" height="10" fill="#1d1d1d"/><path d="M0 0l7 6 7-6" fill="none" stroke="#acd037"/></svg>hello@sunnysidecare.com</li>
      <li><svg width="12" height="12" viewBox="0 0 16 16"><path d="M3 1l3 3-2 2q2 4 6 6l2-2 3 3-2 2Q6 15 1 3z" fill="#1d1d1d"/></svg>+00 555 01 78</li>
      <li><svg width="14" height="14" viewBox="0 0 14 14"><path d="M6 8 8 6M5 6 3 8a2 2 0 0 0 3 3l2-2M9 8l2-2a2 2 0 0 0-3-3L6 5" fill="none" stroke="#1d1d1d" stroke-width="1.5"/></svg>www.sunnysidecare.com</li>
    </ul>
    <div class="foot-icons"><span></span><span></span><span></span><span></span><span></span><span></span></div>
  </div>
  <div class="abs col" style="left:943px">
    <div class="foot-title">Main Links</div>
    <ul><li>Delivery Time</li><li>Order Tracking</li><li>Shopping Cart</li><li>My Account</li><li>Secure Payment</li></ul>
  </div>
  <div class="abs btn-dark">Read More</div>
</footer>

<div class="abs copyright">Copyright © 2016 sunnysideurgentcare | All Rights Reserved</div>

</body>
</html>
```